A Freight forwarding (transportation/shipping) company requires stationary designs

We need The following:
1. Letterhead
2. Letter Envelope
3. Business Card Design
4. A4 Paper Envelope
5. A4 Paper Folder (One that is 2xA4 foldable size which we can open in half and we can put a paper in between and has a lot for business card)
6. A5 Paper (To be used for notes taking)
a design for a freight forwarding company named KORVELA MIND INTERNATIONAL TRANSPORTATION.
(We are active in Sea Transportation, Truck transportation, and Air Transportation, (printed design in PDF is required with all open source files for editing - lamination accepted)
Playing around with the Logo is accepted,, Korvela Logo.png is the correct logo.
Example of folder, envelopes, and notepad attached
Address of the company is :
No 7, 4th Tarandil Gharbi, Neshat Lar Blvd,
Mashhad, IR
Tel : +98 51 37412958
Fax : +98 51 37490316
Website : www.korvela-example.com
Email : info@korvela-example.com

```html
<!DOCTYPE html>
<html lang="en">
<head>
<meta charset="utf-8">
<title>Korvela Mind – Business Card</title>
<link rel="stylesheet" href="https://fonts.googleapis.com/css2?family=Open+Sans:wght@400;600;700&display=swap">
<style>
  :root {
    --bg: #e9eaec;
    --card-white: #f7f7f7;
    --brand-green: #3f9440;
    --brand-blue: #3a3aa0;
    --text-grey: #555555;
    --title-green: #3f9a3f;
    --divider: #c4c4c4;
    --ink: #222222;
  }
  * { margin: 0; padding: 0; box-sizing: border-box; }
  html, body {
    width: 1200px; height: 960px; overflow: hidden;
    background: var(--bg);
    font-family: "Open Sans", Arial, sans-serif;
  }
  .stage { position: relative; width: 1200px; height: 960px; }
  .card {
    position: absolute; left: 180px; width: 840px; height: 440px;
    border-radius: 4px; overflow: hidden;
    box-shadow: 0 6px 18px rgba(0,0,0,.18);
  }
  /* back */
  .card--back { top: 30px; background: var(--brand-green); color: #fff; }
  .back-brand {
    position: absolute; left: 0; right: 0; top: 120px;
    display: flex; flex-direction: column; align-items: center;
  }
  .back-brand .mark-dot {
    width: 96px; height: 96px; border-radius: 50%;
    border: 4px solid #fff; margin-bottom: 18px;
  }
  .back-brand .name { font-size: 30px; font-weight: 600; letter-spacing: .5px; }
  .back-brand .tagline { font-size: 15px; margin-top: 2px; }
  .back-web {
    position: absolute; left: 0; right: 0; bottom: 34px; text-align: center;
    font-size: 16px; letter-spacing: 6px; opacity: .85;
  }
  /* front */
  .card--front { top: 500px; background: var(--card-white); }
  .side-tab {
    position: absolute; top: 60px; width: 16px; height: 320px;
    background: var(--brand-blue);
  }
  .side-tab--left { left: 0; border-radius: 0 10px 10px 0; top: 30px; }
  .side-tab--right { right: 0; border-radius: 10px 0 0 10px; top: 110px; }
  .front-brand {
    position: absolute; left: 70px; top: 90px; width: 300px;
    display: flex; flex-direction: column; align-items: center;
  }
  .front-brand .mark-dot {
    width: 150px; height: 150px; border-radius: 50%;
    border: 14px solid var(--brand-blue); margin-bottom: 16px;
  }
  .front-brand .name { font-size: 30px; font-weight: 400; color: var(--ink); letter-spacing: .3px; }
  .front-brand .tagline { font-size: 14px; font-weight: 600; color: var(--ink); margin-top: -2px; }
  .divider {
    position: absolute; left: 415px; top: 70px; width: 1px; height: 300px;
    background: linear-gradient(to bottom, transparent, var(--divider) 20%, var(--divider) 80%, transparent);
  }
  .contact { position: absolute; left: 455px; top: 92px; color: var(--text-grey); }
  .contact .person { font-size: 24px; font-weight: 700; color: var(--brand-blue); line-height: 1.1; }
  .contact .role { font-size: 20px; color: var(--title-green); margin-bottom: 10px; }
  .contact .address { font-size: 19px; line-height: 1.3; margin-bottom: 4px; }
  .contact ul { list-style: none; }
  .contact li { font-size: 19px; line-height: 1.35; display: flex; align-items: center; gap: 10px; }
  .contact li svg { width: 16px; height: 16px; fill: var(--brand-blue); flex: none; }
  .contact li.plain { padding-left: 26px; }
</style>
</head>
<body>
<main class="stage">
  <section class="card card--back">
    <div class="back-brand">
      <div class="mark-dot"></div>
      <div class="name">KORVELA MIND</div>
      <div class="tagline">International Transportation</div>
    </div>
    <div class="back-web">www.korvela-example.com</div>
  </section>

  <section class="card card--front">
    <span class="side-tab side-tab--left"></span>
    <span class="side-tab side-tab--right"></span>
    <div class="front-brand">
      <div class="mark-dot"></div>
      <div class="name">KORVELA MIND</div>
      <div class="tagline">International Transportation</div>
    </div>
    <div class="divider"></div>
    <div class="contact">
      <div class="person">DARIN HOLT</div>
      <div class="role">CEO/FOUNDER</div>
      <div class="address">No 7, 4th Tarandil Gharbi<br>Neshat Lar Blvd,<br>Mashhad, IR</div>
      <ul>
        <li><svg viewBox="0 0 16 16" aria-hidden="true"><path d="M3.6 1.2l2.3 2.8-1.3 1.9c.9 2 2.5 3.6 4.5 4.5l1.9-1.3 2.8 2.3-1.4 2.4C7.3 14.2 1.8 8.7 1.2 2.6z"/></svg>+98 51 37412958</li>
        <li><svg viewBox="0 0 16 16" aria-hidden="true"><rect x="4" y="1" width="8" height="4"/><rect x="1" y="6" width="14" height="6" rx="1"/><rect x="4" y="10" width="8" height="5"/></svg>+98 51 37490316</li>
        <li><svg viewBox="0 0 16 16" aria-hidden="true"><rect x="1" y="3" width="14" height="10" rx="1"/><path d="M1.5 4l6.5 5 6.5-5" fill="none" stroke="#fff" stroke-width="1.4"/></svg>info@korvela-example.com</li>
        <li><svg viewBox="0 0 16 16" aria-hidden="true"><circle cx="8" cy="8" r="7"/></svg>www.korvela-example.com</li>
      </ul>
    </div>
  </section>
</main>
</body>
</html>
```